We are a building company that build new homes and units we are looking for something fresh and looks good my company name is
Larkmoor Building Group Pty Ltd

Industry/Entity Type

Building

Contact Information for Business Card

Name Marco Delacruz-Fenn
Tittle: Director
Address 14 Quarrel St. Thornbury Vic 3071
Ph: 03 9612 4087
Mobile : 0400 562 938

www.larkmoorbuildinggroup.com.au
Email: sales@larkmoorbuildinggroup.com.au

```html
<!DOCTYPE html>
<html lang="en">
<head>
<meta charset="utf-8">
<title>Larkmoor Building Group – Business Card</title>
<link rel="stylesheet" href="https://fonts.googleapis.com/css2?family=Source+Sans+3:wght@400;600&display=swap">
<style>
  :root {
    --page-bg: #e6e4e1;
    --card-front-top: #f3f3f2;
    --card-front-bottom: #e4e1e1;
    --card-dark: #000000;
    --ink: #1c1c1c;
    --accent-blue: #2f7fc6;
    --brand-grey: #d9dadb;
  }
  * { box-sizing: border-box; margin: 0; padding: 0; }
  html, body {
    width: 1200px; height: 970px; overflow: hidden;
    background: var(--page-bg);
    font-family: "Source Sans 3", "Myriad Pro", sans-serif;
  }
  .business-card {
    position: absolute; left: 100px; top: 207px;
    width: 1000px; height: 556px;
    display: flex;
    box-shadow: 0 10px 30px rgba(0,0,0,0.18);
  }
  .contact-side {
    position: relative;
    width: 497px; height: 100%;
    background: linear-gradient(180deg, var(--card-front-top) 0%, var(--card-front-top) 55%, var(--card-front-bottom) 100%);
    color: var(--ink);
  }
  .brand-side {
    position: relative;
    flex: 1; height: 100%;
    background: var(--card-dark);
    display: flex; align-items: center; justify-content: center;
  }
  .brand-side .notch {
    position: absolute; left: -18px; top: 96px;
    width: 0; height: 0;
    border-top: 16px solid transparent;
    border-bottom: 16px solid transparent;
    border-right: 18px solid var(--card-dark);
  }
  .person-name {
    position: absolute; left: 68px; top: 86px;
    font-size: 36px; font-weight: 400; letter-spacing: -0.2px;
    white-space: nowrap;
  }
  .person-name .first-name { color: var(--accent-blue); }
  .person-title {
    position: absolute; left: 68px; top: 140px;
    font-size: 27px;
  }
  .contact-list {
    position: absolute; left: 64px; top: 232px;
    list-style: none;
  }
  .contact-list li {
    display: flex; align-items: flex-start;
    font-size: 28px; line-height: 36px;
    margin-bottom: 11px;
    white-space: nowrap;
  }
  .contact-list li.small { font-size: 24px; margin-bottom: 10px; }
  .contact-list .icon {
    width: 26px; height: 36px; flex: none; margin-right: 10px;
    display: flex; align-items: center; justify-content: center;
  }
  .contact-list .icon svg { fill: var(--ink); }
  .brand-name {
    color: var(--brand-grey);
    font-size: 34px; font-weight: 600;
    text-align: center; line-height: 1.2;
    margin-top: 40px;
  }
</style>
</head>
<body>
  <section class="business-card">
    <div class="contact-side">
      <h1 class="person-name"><span class="first-name">Marco</span> Delacruz-Fenn</h1>
      <p class="person-title">Director</p>
      <ul class="contact-list">
        <li>
          <span class="icon"><svg width="18" height="26" viewBox="0 0 18 26"><path d="M9 0C4 0 0 4 0 9c0 7 9 17 9 17s9-10 9-17c0-5-4-9-9-9zm0 12.5A3.5 3.5 0 1 1 9 5.5a3.5 3.5 0 0 1 0 7z"/></svg></span>
          <span>14 Quarrel St. Thornbury<br>Vic 3071</span>
        </li>
        <li>
          <span class="icon"><svg width="22" height="22" viewBox="0 0 24 24"><path d="M6.6 10.8a15 15 0 0 0 6.6 6.6l2.2-2.2c.3-.3.7-.4 1-.2 1.1.4 2.3.6 3.6.6.6 0 1 .4 1 1V20c0 .6-.4 1-1 1A17 17 0 0 1 3 4c0-.6.4-1 1-1h3.5c.6 0 1 .4 1 1 0 1.3.2 2.5.6 3.6.1.3 0 .7-.2 1z"/></svg></span>
          <span>03 9612 4087</span>
        </li>
        <li>
          <span class="icon"><svg width="16" height="28" viewBox="0 0 16 28"><path d="M2 0h12a2 2 0 0 1 2 2v24a2 2 0 0 1-2 2H2a2 2 0 0 1-2-2V2a2 2 0 0 1 2-2zm1 3v11h10V3zm1 14v2h2v-2zm3 0v2h2v-2zm3 0v2h2v-2zm-6 3v2h2v-2zm3 0v2h2v-2zm3 0v2h2v-2z" fill-rule="evenodd"/></svg></span>
          <span>0400 562 938</span>
        </li>
        <li class="small">
          <span class="icon"><svg width="18" height="13" viewBox="0 0 18 13"><path d="M0 0h18v13H0zm1.5 1.5v.3L9 7l7.5-5.2v-.3zm0 2.1V11.5h15V3.6L9 8.8z" fill-rule="evenodd"/></svg></span>
          <span>sales@larkmoorbuildinggroup.com.au</span>
        </li>
        <li class="small">
          <span class="icon"><svg width="18" height="18" viewBox="0 0 18 18"><path d="M9 0a9 9 0 1 0 0 18A9 9 0 0 0 9 0zm6.9 8h-3a14 14 0 0 0-1.1-5.4A7 7 0 0 1 15.9 8zM9 2.1c.8 1 1.8 3 1.9 5.9H7.1C7.2 5.1 8.2 3.1 9 2.1zM6.2 2.6A14 14 0 0 0 5.1 8h-3a7 7 0 0 1 4.1-5.4zM2.1 10h3a14 14 0 0 0 1.1 5.4A7 7 0 0 1 2.1 10zM9 15.9c-.8-1-1.8-3-1.9-5.9h3.8c-.1 2.9-1.1 4.9-1.9 5.9zm2.8-.5a14 14 0 0 0 1.1-5.4h3a7 7 0 0 1-4.1 5.4z"/></svg></span>
          <span>www.larkmoorbuildinggroup.com.au</span>
        </li>
      </ul>
    </div>
    <div class="brand-side">
      <span class="notch"></span>
      <p class="brand-name">Larkmoor<br>Building Group Pty Ltd</p>
    </div>
  </section>
</body>
</html>
```